Jazz: Journey Through the Harlem Renaissance and the Black Arts Movement

Corvel Tavern invites you on a musical Journey Through the Harlem Renaissance and the Black Arts Movement!
Join us for an afternoon of Jazz on Sunday, February 27, 2022 from 3pm – 5pm.
Local jazz artists will thrill you with the music of legendary Harlem Renaissance artists such as Royce Tamberlin and Odessa Crane and famed Black Arts Movement stylings reminiscent of Vernon Askew and Lydia Farrow.
There will be games, prizes and opportunities to support arts programs at local schools.

```html
<!DOCTYPE html>
<html lang="en">
<head>
<meta charset="utf-8">
<title>Corvel Tavern – A Musical Journey</title>
<link href="https://fonts.googleapis.com/css2?family=Oswald:wght@400;500;600;700&display=swap" rel="stylesheet">
<style>
  :root {
    --page: #5b5b5b;
    --ink: #050505;
    --white: #ffffff;
    --gold: #ffd21f;
    --gold-deep: #c9971a;
    --gold-light: #ffd84a;
    --photo-light: #cfcfcf;
    --photo-dark: #2a2a2a;
  }
  * { box-sizing: border-box; margin: 0; padding: 0; }
  html, body {
    width: 1200px; height: 1200px; overflow: hidden;
    background: var(--page);
    font-family: "Oswald", "Arial Narrow", sans-serif;
  }
  .flyer {
    position: absolute; left: 191px; top: 20px;
    width: 842px; height: 1192px;
    background: var(--ink);
    transform: scale(0.973); transform-origin: top left;
  }
  .headline {
    position: absolute; left: 0; right: 0;
    text-align: center; text-transform: uppercase; line-height: 1;
    white-space: nowrap;
  }
  .headline--intro { top: 46px; font-size: 45px; font-weight: 500; color: var(--white); letter-spacing: -0.5px; }
  .headline--main { top: 104px; font-size: 62px; font-weight: 700; color: var(--gold); letter-spacing: -0.5px; }
  .headline--sub { top: 188px; font-size: 30px; font-weight: 600; color: var(--white); letter-spacing: -0.4px; }

  .artists { position: absolute; left: 49px; top: 244px; width: 742px; height: 471px; display: flex; gap: 2px; }
  .artist { position: relative; flex: 1; overflow: hidden; }
  .artist__photo {
    position: absolute; inset: 0;
    background: linear-gradient(180deg, var(--photo-light) 0%, #8d8d8d 45%, var(--photo-dark) 100%);
  }
  .artist__tag {
    position: absolute; right: -40px; bottom: 28px; width: 250px; height: 26px;
    background: var(--gold); color: var(--ink);
    transform: rotate(-30deg); transform-origin: center;
    font-size: 16px; font-weight: 500; line-height: 26px; text-align: center;
    padding-left: 40px; white-space: nowrap;
  }

  .date-band {
    position: absolute; left: 0; right: 0; top: 732px; height: 148px;
    background: linear-gradient(90deg, var(--gold-deep) 0%, var(--gold-light) 50%, var(--gold-deep) 100%);
    display: flex; flex-direction: column; justify-content: center; align-items: center;
    color: var(--ink); text-transform: uppercase; font-weight: 600; font-size: 39px; line-height: 1.25; letter-spacing: -0.5px;
    white-space: nowrap;
  }

  .details {
    position: absolute; left: 49px; top: 910px; width: 540px;
    color: var(--white); font-size: 26px; font-weight: 400; line-height: 1.42; letter-spacing: -0.4px;
    white-space: nowrap;
  }
  .details .hl { color: var(--gold); font-size: 29px; }
  .details .lead { color: var(--gold); }

  .venue-mark {
    position: absolute; left: 600px; top: 922px; width: 200px; height: 160px;
    display: flex; flex-direction: column; align-items: center; justify-content: center; gap: 12px;
  }
  .venue-mark svg { display: block; }
  .venue-mark__name { color: var(--gold); font-size: 30px; font-weight: 500; text-transform: uppercase; letter-spacing: 1px; white-space: nowrap; }

  .footer-band {
    position: absolute; left: 0; right: 0; top: 1124px; height: 48px;
    background: linear-gradient(90deg, var(--gold-deep) 0%, var(--gold-light) 50%, var(--gold-deep) 100%);
    color: var(--ink); font-size: 20px; font-weight: 500; line-height: 48px; text-align: center; letter-spacing: -0.2px;
    white-space: nowrap;
  }
</style>
</head>
<body>
  <main class="flyer">
    <h2 class="headline headline--intro">Corvel Tavern invites you on</h2>
    <h1 class="headline headline--main">A Musical Journey Through</h1>
    <h2 class="headline headline--sub">The Harlem Renaissance and the Black Arts Movement!</h2>

    <section class="artists">
      <figure class="artist">
        <div class="artist__photo" role="img" aria-label="Black and white portrait of Royce Tamberlin"></div>
        <figcaption class="artist__tag">Royce Tamberlin</figcaption>
      </figure>
      <figure class="artist">
        <div class="artist__photo" role="img" aria-label="Black and white portrait of Odessa Crane with a flower in her hair"></div>
        <figcaption class="artist__tag">Odessa Crane</figcaption>
      </figure>
      <figure class="artist">
        <div class="artist__photo" role="img" aria-label="Black and white portrait of Vernon Askew holding a saxophone"></div>
        <figcaption class="artist__tag">Vernon Askew</figcaption>
      </figure>
      <figure class="artist">
        <div class="artist__photo" role="img" aria-label="Black and white portrait of Lydia Farrow smiling"></div>
        <figcaption class="artist__tag">Lydia Farrow</figcaption>
      </figure>
    </section>

    <section class="date-band">
      <p>Join us for an afternoon of jazz on Sunday,</p>
      <p>February 27, 2022 from 3pm – 5pm.</p>
    </section>

    <p class="details">
      <span class="lead">Local jazz artists will thrill you with</span><br>
      the music of legendary Harlem Renaissance<br>
      artists such as <span class="hl">Royce Tamberlin</span> and <span class="hl">Odessa Crane</span><br>
      and famed Black Arts Movement stylings<br>
      reminiscent of <span class="hl">Vernon Askew</span> and <span class="hl">Lydia Farrow</span>.
    </p>

    <div class="venue-mark">
      <svg width="40" height="40" viewBox="0 0 40 40" aria-hidden="true">
        <circle cx="20" cy="20" r="17" fill="none" stroke="var(--gold)" stroke-width="3"/>
      </svg>
      <span class="venue-mark__name">Corvel Tavern</span>
    </div>

    <p class="footer-band">There will be games, prizes &amp; opportunities to support arts programs at local schools.</p>
  </main>
</body>
</html>
```